Product sheet for managing talented people!

We need a new product sheet to describe our method of helping organisations to manage their talented people! We have selected a rowing team as the graphical theme (sample attached - please select or suggest a new picture if you want). We have also attached a powerpoint slide with our model (this is the service we offer).

FRONT PAGE

We are looking for an eye-catching front page that uses our 1. "Kestrel Growth Model"; 2. a picture of a rowing team of 8, and 3. our logo and 1800 KESTRL phone number (1800 537 875).

Step 1 - Assess key positions to determine your Talent Management Priorities.

Step 2 - Organisational psychology support helps individuals self-evaluate (see page 2 for details).

Step 3 - Facilitate agreement with manager and embed best-practice in organisational fairness.

Step 4 - Tailor career development and redeployment options based on shared understanding.

Step 5 - Evaluate ROI for individual performance and engagement.

BACK PAGE

The second page will have more detail of each of the talent categories also included in the powerpoint slide. Logo attached also. Please also view our website as the graphics should give you a sense of the look and feel of our brand - www.kestrelgm.com.au We have also added another flyer that we still use - please do not reverse the logo on this project - use in current form. CORPORATE LOGO / COLOUR GUIDE
C100 M50 Y0 K0
C100 M50 Y0 K0
C100 M50 Y0 K0
Gradient
C100 M60 Y0 K40
C100 M45 Y0 K0
C100 M20 Y0 K0
C70 M0 Y0 K0
PMS 2935 C
PMS 2935 C 75% Tint
PMS 2935 C
PMS Process Cyan C

The successful flyer will need to be print ready (as per attached example) and in pdf form so that we can print and/or send as a PDF.

Thanks.

Target Market(s)

Human Resource Managers in business and government.

Industry/Entity Type

Product

Requirements
Must have
• Eye-catching graphics with a rowing team theme. Colours consistent with our corporate colour codes.
Nice to have
• Please add small "trademark" symbol to the logo. This is small TM in a circle and usually placed at top right hand of logo. PLease add our website address www.kestrelgm.com
Should not have
• Please do not "reverse" the logo - use as is.

```html
<!DOCTYPE html>
<html lang="en">
<head>
<meta charset="utf-8">
<title>Kestrel Growth Management – Product Sheet</title>
<link rel="stylesheet" href="https://fonts.googleapis.com/css2?family=Mulish:wght@400;600;700;800&display=swap">
<style>
  :root {
    --backdrop: #d8c9ab;
    --sheet-grey: #e8e9ec;
    --white: #ffffff;
    --navy: #134a7c;
    --navy-deep: #0f3f6d;
    --indigo: #3b4c9e;
    --water-light: #7fb0ba;
    --water-dark: #2f6f7c;
    --lake-top: #8fa7b9;
    --lake-bottom: #c9d3dd;
    --text-blue: #1d4f86;
    --call-blue: #1565b8;
    --tab-blue: #2a7cc0;
  }
  * { box-sizing: border-box; margin: 0; padding: 0; }
  html, body { width: 1200px; height: 829px; overflow: hidden; }
  body {
    background: var(--backdrop);
    font-family: "Mulish", sans-serif;
    position: relative;
  }

  .sheet {
    position: absolute;
    background: var(--sheet-grey);
    box-shadow: 0 4px 14px rgba(70, 55, 30, 0.25);
    overflow: hidden;
  }
  .sheet--front { left: 66px; top: 81px; width: 447px; height: 667px; }
  .sheet--back  { left: 617px; top: 82px; width: 446px; height: 684px; }

  .edge-bar { position: absolute; height: 7px; background: var(--indigo); }

  /* Front */
  .front-header { position: absolute; left: 0; top: 0; width: 100%; height: 152px; background: var(--white); }
  .front-header .edge-bar { left: 0; top: 0; width: 292px; }
  .headline {
    position: absolute; left: 36px; top: 99px;
    font-weight: 800; font-size: 17.5px; line-height: 24px;
    color: var(--navy); text-transform: uppercase;
    transform: rotate(-2deg); transform-origin: left top;
  }
  .brand {
    position: absolute; left: 320px; top: 76px;
    display: flex; align-items: center; gap: 6px;
  }
  .brand-dot { width: 10px; height: 10px; background: var(--navy); }
  .brand-name {
    font-weight: 700; font-size: 20px; color: var(--navy); letter-spacing: 0.5px;
  }
  .brand-tm { font-size: 7px; font-weight: 700; color: var(--navy); align-self: flex-start; }
  .brand-sub {
    position: absolute; left: 333px; top: 103px;
    font-size: 6px; font-weight: 700; color: var(--navy); letter-spacing: 1px;
  }

  .front-photo {
    position: absolute; left: 0; top: 152px; width: 100%; height: 298px;
    background: linear-gradient(160deg, var(--water-light), var(--water-dark) 70%, #3d7d88);
  }

  .steps { position: absolute; left: 28px; top: 399px; width: 391px; list-style: none; }
  .step {
    position: relative; height: 30px; margin-bottom: 7px;
    background: var(--navy); border-radius: 6px;
    color: var(--white); font-weight: 700; font-size: 8.2px;
    white-space: nowrap;
    display: flex; align-items: center; padding-left: 18px;
    transform: rotate(-2.2deg);
  }
  .step::before {
    content: ""; position: absolute; left: -6px; top: 13px;
    width: 8px; height: 5px; border-radius: 3px; background: var(--tab-blue);
  }

  .call-button {
    position: absolute; left: 204px; top: 604px; width: 219px; height: 34px;
    background: var(--call-blue); border-radius: 17px;
    color: var(--white); font-weight: 800; font-size: 11.5px;
    display: flex; align-items: center; justify-content: center;
    transform: rotate(-2deg);
  }
  .front-url {
    position: absolute; left: 20px; top: 652px;
    font-size: 10.5px; font-weight: 700; color: var(--navy);
  }
  .sheet--front .edge-bar--foot { left: 144px; bottom: 0; width: 303px; }

  /* Back */
  .sheet--back .edge-bar--top { left: 0; top: 0; width: 301px; z-index: 2; }
  .back-photo {
    position: absolute; left: 0; top: 6px; width: 100%; height: 240px;
    background: linear-gradient(180deg, #5b7a66 0%, var(--lake-top) 12%, #9fb2c1 55%, var(--lake-bottom) 85%, var(--sheet-grey) 100%);
  }
  .back-title {
    position: absolute; left: 35px; top: 228px;
    font-weight: 800; font-size: 21px; line-height: 24px; color: var(--navy);
    transform: rotate(-1.5deg); transform-origin: left top;
  }
  .back-lead {
    position: absolute; left: 35px; top: 254px; width: 340px;
    font-size: 14px; line-height: 17.5px; color: var(--text-blue);
    transform: rotate(-2deg); transform-origin: left top;
  }
  .categories { position: absolute; left: 30px; top: 300px; width: 388px; list-style: none; }
  .category {
    height: 31px; margin-bottom: 7.5px;
    background: var(--navy-deep); border-radius: 5px;
    color: var(--white); font-weight: 700; font-size: 11.5px;
    display: flex; align-items: center; padding-left: 13px;
    transform: rotate(-1.2deg);
  }
  .back-summary {
    position: absolute; left: 32px; top: 552px; width: 330px;
    font-size: 13.5px; line-height: 17px; color: var(--text-blue);
    transform: rotate(-2deg); transform-origin: left top;
  }
  .sheet--back .edge-bar--foot { left: 145px; bottom: 0; width: 301px; height: 8px; }
</style>
</head>
<body>

<section class="sheet sheet--front">
  <header class="front-header">
    <div class="edge-bar"></div>
    <h1 class="headline">Get your team heading<br>in the right direction!</h1>
    <div class="brand">
      <span class="brand-dot"></span>
      <span class="brand-name">KESTREL</span>
      <span class="brand-tm">™</span>
    </div>
    <div class="brand-sub">GROWTH MANAGEMENT</div>
  </header>

  <div class="front-photo" role="img" aria-label="Aerial photo of an eight-person rowing crew on green-blue water"></div>

  <ol class="steps">
    <li class="step">Assess Key Positions To Determine Your Talent Management Priorities</li>
    <li class="step">Organisational Psychology Support Helps Individuals Self-evaluate</li>
    <li class="step">Facilitate Agreement With Manager And Embed Best-practice In Organisational Fairness</li>
    <li class="step">Tailor Career Development And Redeployment Options Based On Shared Understanding</li>
    <li class="step">Evaluate Roi For Individual Performance And Engagement</li>
  </ol>

  <div class="call-button">CALL 1800 KESTRL (1800 537 875)</div>
  <div class="front-url">www.kestrelgm.com.au</div>
  <div class="edge-bar edge-bar--foot"></div>
</section>

<section class="sheet sheet--back">
  <div class="edge-bar edge-bar--top"></div>
  <div class="back-photo" role="img" aria-label="Photo of a women's rowing crew racing on a lake, fading into the page"></div>

  <h2 class="back-title">TALENT ASSESSMENT</h2>
  <p class="back-lead">Help your people find their perfect role and<br>develop their skills in a fair process</p>

  <ul class="categories">
    <li class="category">Exit – planned or managed</li>
    <li class="category">Developing - high risk/high reward</li>
    <li class="category">Contributing - probable flight risk</li>
    <li class="category">Emerging – manage career aspirations</li>
    <li class="category">Elite – mission critical or market-sensitive</li>
    <li class="category">Target – strategic external hire with market implications</li>
  </ul>

  <p class="back-summary">Kestrel Growth Management provides first-class organisational psychology services to ensure that your key staff are supported, developed, retained and in the right roles</p>
  <div class="edge-bar edge-bar--foot"></div>
</section>

</body>
</html>
```